Specialised investor in e-mobility and energy wants business card design

We need a business card design that fits our existing corporate design. <The look and feel must be 'sharp'/'clean', dynamic, communicate momentum, professionalism etc (as one would imagine from a firm in the financial sector). We like the idea of a reverse-side of the card that includes the logo, and the name and contact details on the other. We expect the deliverable to be whatever format might be required to be able to get cards printed directly by a service such as marlo cards. Our website is www.obrel.finance

```html
<!DOCTYPE html>
<html lang="en">
<head>
<meta charset="utf-8">
<title>Obrel Finance – Business Card</title>
<link rel="stylesheet" href="https://fonts.googleapis.com/css2?family=Montserrat:wght@400;700&display=swap">
<style>
  :root {
    --ground: #d9d9d6;
    --card: #ffffff;
    --green-dark: #2f4f22;
    --green-light: #84b545;
    --ink: #2b2b2b;
  }
  * { margin: 0; padding: 0; box-sizing: border-box; }
  html, body { width: 1200px; height: 801px; overflow: hidden; }
  body {
    background: var(--ground);
    font-family: "Montserrat", sans-serif;
    position: relative;
  }
  .card {
    position: absolute;
    top: 232px;
    width: 520px;
    height: 336px;
    background: var(--card);
    border-bottom: 3px solid var(--green-light);
    overflow: hidden;
  }
  .card--front { left: 50px; }
  .card--back { left: 630px; }

  .wave { position: absolute; inset: 0; width: 100%; height: 100%; }

  .brand-name {
    position: absolute;
    display: flex;
    align-items: center;
    gap: 10px;
    color: var(--green-dark);
    font-weight: 400;
    white-space: nowrap;
  }
  .brand-dot {
    border-radius: 50%;
    background: var(--green-dark);
    flex: none;
  }
  .card--front .brand-name { left: 36px; top: 146px; font-size: 24px; }
  .card--front .brand-dot { width: 14px; height: 14px; }
  .card--back .brand-name {
    left: 0; right: 0; top: 138px;
    justify-content: center;
    font-size: 48px;
  }
  .card--back .brand-dot { width: 26px; height: 26px; }

  .divider {
    position: absolute;
    left: 252px; top: 52px;
    width: 1px; height: 200px;
    background: var(--green-light);
  }
  .details {
    position: absolute;
    left: 272px; top: 52px;
    color: var(--ink);
  }
  .person-name {
    color: var(--green-light);
    font-weight: 700;
    font-size: 18px;
    letter-spacing: 0.5px;
    line-height: 22px;
  }
  .person-role { font-size: 13px; line-height: 18px; }
  .contacts { list-style: none; margin-top: 16px; }
  .contacts li {
    display: flex; align-items: center; gap: 8px;
    font-size: 12px; line-height: 19px;
  }
  .contacts svg { width: 11px; height: 11px; fill: var(--green-light); flex: none; }
  .company {
    margin-top: 14px;
    color: var(--green-light);
    font-size: 13px; line-height: 18px;
  }
  .city { font-size: 13px; line-height: 18px; }
</style>
</head>
<body>

<section class="card card--front">
  <svg class="wave" viewBox="0 0 520 336" aria-hidden="true">
    <path d="M120 336 C250 326 320 290 390 232 S480 160 520 150 V336 Z" fill="var(--green-light)"/>
    <path d="M150 336 C270 328 335 296 402 242 S488 176 520 168 V336 Z" fill="var(--card)"/>
    <path d="M162 336 C280 330 345 300 410 248 S492 184 520 176 V336 Z" fill="var(--green-dark)"/>
  </svg>

  <div class="brand-name"><span class="brand-dot"></span>Obrel Finance</div>
  <div class="divider"></div>

  <div class="details">
    <p class="person-name">MARTEN HOLLOWAY</p>
    <p class="person-role">Managing Director</p>
    <ul class="contacts">
      <li><svg viewBox="0 0 12 12"><path d="M2 1h3l1 3-2 1a7 7 0 0 0 3 3l1-2 3 1v3c-6 0-9-3-9-9z"/></svg>+41 70415 2290</li>
      <li><svg viewBox="0 0 12 12"><path d="M0 2h12v8H0z M0 2l6 5 6-5" /></svg>marten@obrel.finance</li>
      <li><svg viewBox="0 0 12 12"><circle cx="6" cy="6" r="6"/></svg>www.obrel.finance</li>
    </ul>
    <p class="company">Obrel Finance S.A.</p>
    <p class="city">Geneva, Switzerland</p>
  </div>
</section>

<section class="card card--back">
  <div class="brand-name"><span class="brand-dot"></span>Obrel Finance</div>
</section>

</body>
</html>
```